Law Office Business Card

We need a business card design to include the following information:
Name of Firm: Brennick Law Group, P.A.
Address: 4627 Sandlot Ave, Ste 208, Harbor Point, FL 33981
Phone: 561-555-0148
Fax: 561-555-0193
Website: http://www.tbrennicklaw.example

We Need a place for the Person's name and email address. Please start with the following:
Lorna K. Dwyer, Esq.
lorna@tbrennicklaw.example

```html
<!DOCTYPE html>
<html lang="en">
<head>
<meta charset="utf-8">
<title>Brennick Law Group – Business Card</title>
<link href="https://fonts.googleapis.com/css2?family=Cinzel:wght@500;600&family=Cormorant+Garamond:wght@500;600&display=swap" rel="stylesheet">
<style>
  :root {
    --backdrop: #2a2a2a;
    --card: #f7f7f5;
    --card-edge: #e6e5e1;
    --gold: #9c8467;
    --gold-dark: #7d6a52;
    --ink: #26221d;
    --muted: #5d554b;
    --map-a: #e3e1dc;
    --map-b: #f7f7f5;
  }
  * { margin: 0; padding: 0; box-sizing: border-box; }
  html, body { width: 1200px; height: 873px; overflow: hidden; }
  body {
    background: var(--backdrop);
    display: flex; align-items: center; justify-content: center;
    font-family: "Cormorant Garamond", Georgia, serif;
  }
  .card {
    position: relative;
    width: 860px; height: 500px;
    background: linear-gradient(135deg, #ffffff 0%, var(--card) 55%, var(--card-edge) 100%);
    border-radius: 22px;
    box-shadow: 0 24px 50px rgba(0,0,0,.55);
    overflow: hidden;
  }
  .world-map {
    position: absolute; left: 210px; top: 40px; width: 520px; height: 330px;
    background: radial-gradient(ellipse at 50% 45%, var(--map-a) 0%, var(--map-a) 35%, var(--map-b) 72%);
    border-radius: 50%;
    opacity: .85;
  }
  .firm-name {
    position: absolute; left: 56px; top: 108px;
    font-family: "Cinzel", Georgia, serif; font-weight: 500;
    font-size: 27px; letter-spacing: 1px; line-height: 1.15;
    color: var(--gold);
  }
  .firm-name .mark {
    display: inline-block; width: 18px; height: 18px;
    border: 2px solid var(--gold); margin-right: 10px; vertical-align: 1px;
  }
  .person {
    position: absolute; right: 60px; top: 146px;
    font-family: "Cinzel", Georgia, serif; font-weight: 600;
    font-size: 30px; color: var(--ink); letter-spacing: .5px;
  }
  .rule-main {
    position: absolute; left: 56px; right: 60px; top: 196px;
    height: 2px; background: linear-gradient(90deg, var(--gold-dark), var(--gold));
  }
  .role {
    position: absolute; right: 60px; top: 204px;
    font-size: 18px; color: var(--muted);
  }
  .rule-contact {
    position: absolute; left: 56px; top: 290px; width: 190px; height: 2px;
    background: var(--gold-dark);
  }
  .contacts { position: absolute; left: 56px; top: 308px; list-style: none; }
  .contacts li {
    display: flex; align-items: center; gap: 14px;
    height: 40px; font-size: 21px; color: var(--ink); font-weight: 500;
  }
  .contacts svg { width: 28px; height: 28px; flex: none; }
  .website {
    position: absolute; right: 60px; top: 322px;
    font-size: 19px; font-weight: 600; color: var(--gold);
  }
  .address {
    position: absolute; left: 56px; bottom: 38px;
    font-size: 21px; font-weight: 600; color: var(--gold);
  }
</style>
</head>
<body>
  <section class="card">
    <div class="world-map" role="img" aria-label="Faint dotted world map in the background"></div>

    <div class="firm-name"><span class="mark"></span>Brennick Law Group</div>

    <h1 class="person">Lorna K. Dwyer, Esq.</h1>
    <div class="rule-main"></div>
    <p class="role">Lawyer</p>

    <div class="rule-contact"></div>
    <ul class="contacts">
      <li>
        <svg viewBox="0 0 28 28" aria-hidden="true"><circle cx="14" cy="14" r="14" fill="#9c8467"/>
          <path d="M8 12c0-3 3-4 6-4s6 1 6 4l-2 1-1-2h-6l-1 2z M9 15h10l1 5H8z" fill="#fff"/></svg>
        <span>561-555-0148</span>
      </li>
      <li>
        <svg viewBox="0 0 28 28" aria-hidden="true"><circle cx="14" cy="14" r="14" fill="#9c8467"/>
          <rect x="10" y="7" width="8" height="5" fill="#fff"/><rect x="7" y="12" width="14" height="7" rx="1" fill="#fff"/>
          <rect x="10" y="17" width="8" height="4" fill="#fff" stroke="#9c8467"/></svg>
        <span>561-555-0193</span>
      </li>
      <li>
        <svg viewBox="0 0 28 28" aria-hidden="true"><circle cx="14" cy="14" r="14" fill="#9c8467"/>
          <rect x="7" y="9" width="14" height="10" fill="#fff"/><path d="M7 9l7 6 7-6" fill="none" stroke="#9c8467" stroke-width="1.4"/></svg>
        <span>lorna@tbrennicklaw.example</span>
      </li>
    </ul>

    <p class="website">www.tbrennicklaw.example</p>
    <p class="address">4627 Sandlot Ave, Ste 208, Harbor Point, FL 33981</p>
  </section>
</body>
</html>
```